Flyer-Design für Fahrzeugpflege&Lackveredelung
Zielgruppe
Die Firma VK Glanzwerk - Fahrzeugpflege&Lackveredelung ist ein Kleinunternehmen im Car-Detailing Bereich. Hier steht höchste Qualität und maximale Kundenzufriedenheit auf höchster Stelle.
Zielgruppen sind Fahrzeugbesitzer von hochwertigen Wagen, die höchste Ansprüche auf die Fahrzeugaufbereitung legen.
Aber auch das Tagesgeschäft mit Innenraumaufbereitungen für den Normalverbraucher sind möglich.
Aufgabenstellung
Der Flyer soll modern und hochwertig aussehen.
Größe des Flyers: DIN lang (9,8x21)
2-seitig 4/4 farbig
Farben, Daten und Co bitte auf der Internetseite entnehmen
www.vkglanzwerk.de

```html
<!DOCTYPE html>
<html lang="de">
<head>
<meta charset="utf-8">
<title>VK Glanzwerk – Flyer DIN lang</title>
<link href="https://fonts.googleapis.com/css2?family=Raleway:wght@400;500;600;700;800;900&display=swap" rel="stylesheet">
<style>
  :root{
    --bg:#e8e9eb;
    --paper:#ffffff;
    --ink:#4b4b4d;
    --blue:#2f74c0;
    --night:#07080c;
    --white:#ffffff;
  }
  *{margin:0;padding:0;box-sizing:border-box}
  html,body{width:1154px;height:1200px;overflow:hidden;background:var(--bg)}
  body{position:relative;font-family:"Raleway",sans-serif;color:var(--ink)}
  .page{position:absolute;top:48px;width:515px;height:1104px;background:var(--paper);overflow:hidden}
  .page--front{left:40px}
  .page--back{left:598px}
  .art{position:absolute;left:0;top:0}

  /* name plate */
  .brand{position:absolute;display:flex;align-items:center;font-weight:700;letter-spacing:0}
  .brand__square{display:inline-block;background:currentColor;flex:none}
  .brand--front{left:300px;top:112px;color:var(--white);font-size:24px;gap:10px}
  .brand--front .brand__square{width:12px;height:12px}
  .brand--back{left:372px;top:70px;color:var(--night);font-size:16px;gap:7px}
  .brand--back .brand__square{width:8px;height:8px}

  /* front */
  .headline{position:absolute;left:44px;top:546px;font-weight:900;font-size:63px;line-height:53px;letter-spacing:-1px;color:var(--ink);text-transform:uppercase}
  .headline .accent{color:var(--blue)}
  .features{position:absolute;left:50px;top:743px;list-style:none}
  .features li{display:flex;align-items:center;height:45px;font-size:20px;font-weight:500;color:var(--ink)}
  .features .mark{width:27px;height:22px;margin-right:14px;flex:none}
  .features .amp{color:var(--blue)}
  .site{position:absolute;left:51px;top:1018px;font-size:14.5px;font-weight:600;color:var(--blue)}

  /* back */
  .services-title{position:absolute;left:32px;top:38px;font-weight:900;font-size:26px;line-height:25px;letter-spacing:-0.3px;color:var(--ink)}
  .services-title .accent{color:var(--blue)}

  .service-grid{position:absolute;left:0;top:107px;width:515px;display:grid;grid-template-columns:253px 253px;grid-template-rows:169px 169px 169px;column-gap:9px;row-gap:10px}
  .tile{position:relative;display:flex;align-items:center;justify-content:center}
  .tile__label{font-weight:700;font-size:18.5px;color:var(--white);text-shadow:0 1px 3px rgba(0,0,0,.45)}
  .tile--paint{background:linear-gradient(90deg,#2b2a44 0%,#4e4d5e 47%,#8a8a90 48%,#2d2a48 100%)}
  .tile--coat{background:linear-gradient(135deg,#5aa6d9 0%,#1f78c2 45%,#0f4f8f 100%)}
  .tile--interior{background:linear-gradient(180deg,#3a3a3a 0%,#6a4c3a 45%,#2c2c2c 100%)}
  .tile--upholstery{background:linear-gradient(90deg,#b9b7b3 0%,#d3d0cb 49%,#e6e5e2 51%,#c9c8c5 100%)}
  .tile--leather{background:linear-gradient(135deg,#7a7a80 0%,#3a3a3c 40%,#1f1f21 100%)}
  .tile--repair{background:linear-gradient(160deg,#5b5b5b 0%,#8f8c80 40%,#2d2d2d 100%)}

  .more{position:absolute;left:0;top:650px;width:515px;text-align:center}
  .more__title{font-size:15px;font-weight:500;color:var(--ink)}
  .more__list{font-size:13px;font-weight:700;color:var(--blue);line-height:16px;margin-top:2px}

  .offer{position:absolute;left:0;top:716px;width:515px;text-align:center;font-size:15px;font-weight:800;color:var(--ink)}
  .price{position:absolute;left:182px;top:738px;width:160px;height:62px;color:var(--blue);font-weight:800}
  .price__num{position:absolute;left:0;top:0;font-size:72px;line-height:62px;letter-spacing:-3px}
  .price__star{position:absolute;left:128px;top:-2px;font-size:16px;line-height:16px}
  .price__cur{position:absolute;left:120px;top:22px;font-size:34px;line-height:34px}
  .footnote{position:absolute;left:0;top:811px;width:515px;text-align:center;font-size:8.5px;line-height:11px;color:var(--ink)}

  .contact{position:absolute;left:39px;top:950px;color:var(--white);font-size:15px;font-weight:500}
  .contact__owner{font-weight:600;margin-bottom:14px}
  .contact__addr{line-height:19px}
  .contact__row{display:flex;align-items:center;gap:9px;margin-top:9px;height:20px}
  .contact__row svg{width:15px;height:15px;flex:none}
  .contact__site{position:absolute;left:236px;top:1056px;color:var(--white);font-size:15px;font-weight:600}
</style>
</head>
<body>

<section class="page page--front">
  <svg class="art" width="515" height="1104" viewBox="0 0 515 1104">
    <defs>
      <linearGradient id="carTop" x1="0" y1="0" x2="1" y2="1">
        <stop offset="0" stop-color="#2a2b30"/>
        <stop offset=".5" stop-color="#8c8e96"/>
        <stop offset="1" stop-color="#15161a"/>
      </linearGradient>
      <linearGradient id="polish" x1="0" y1="0" x2="1" y2="1">
        <stop offset="0" stop-color="#2d3036"/>
        <stop offset=".55" stop-color="#1a1b1f"/>
        <stop offset=".75" stop-color="#8f8f3a"/>
        <stop offset="1" stop-color="#2b3038"/>
      </linearGradient>
      <linearGradient id="carBottom" x1="1" y1="0" x2="0" y2="1">
        <stop offset="0" stop-color="#dadada"/>
        <stop offset=".6" stop-color="#f4f4f4"/>
        <stop offset="1" stop-color="#ffffff" stop-opacity="0"/>
      </linearGradient>
    </defs>
    <polygon points="0,0 515,0 515,543 0,280" fill="var(--night)"/>
    <path d="M0 30 Q80 20 140 90 L150 210 L0 280 Z" fill="url(#carTop)" opacity=".55" role="img" aria-label="Foto: Front eines dunklen Sportwagens"/>
    <polygon points="394,179 514,251 376,490 349,490" fill="var(--blue)"/>
    <polygon points="32,375 113,231 340,170 487,252 315,533" fill="var(--white)"/>
    <polygon points="42,372 118,240 338,180 476,256 311,522" fill="url(#polish)" role="img" aria-label="Foto: Hand mit Poliermaschine auf Autolack"/>
    <polyline points="90,330 198,266 240,290" fill="none" stroke="var(--white)" stroke-width="1"/>
    <polyline points="418,418 484,454 437,533" fill="none" stroke="var(--white)" stroke-width="1"/>
    <polyline points="418,418 348,450 313,510 380,538" fill="none" stroke="var(--white)" stroke-width="1"/>
    <rect x="300" y="800" width="215" height="304" fill="url(#carBottom)" role="img" aria-label="Foto: weißer Sportwagen mit Felge, Frontansicht"/>
  </svg>

  <div class="brand brand--front"><span class="brand__square"></span>VK Glanzwerk</div>

  <h1 class="headline">The only<br><span class="accent">Car Detailer</span><br>you need.</h1>

  <ul class="features">
    <li><svg class="mark" viewBox="0 0 27 22"><polygon points="0,7 17,0 27,5 18,22" fill="var(--blue)"/></svg>Keramikbeschichtung</li>
    <li><svg class="mark" viewBox="0 0 27 22"><polygon points="0,7 17,0 27,5 18,22" fill="var(--blue)"/></svg>Lackkorrektur</li>
    <li><svg class="mark" viewBox="0 0 27 22"><polygon points="0,7 17,0 27,5 18,22" fill="var(--blue)"/></svg>Innenraumaufbereitung</li>
    <li><svg class="mark" viewBox="0 0 27 22"><polygon points="0,7 17,0 27,5 18,22" fill="var(--blue)"/></svg>Lederpflege&nbsp;<span class="amp">&amp;</span>&nbsp;Reparatur</li>
    <li><svg class="mark" viewBox="0 0 27 22"><polygon points="0,7 17,0 27,5 18,22" fill="var(--blue)"/></svg>Scheibenversiegelung</li>
  </ul>

  <p class="site">www.vkglanzwerk.de</p>
</section>

<section class="page page--back">
  <h2 class="services-title">WAS KANN ICH FÜR<br><span class="accent">DEIN FAHRZEUG</span> TUN?</h2>
  <div class="brand brand--back"><span class="brand__square"></span>VK Glanzwerk</div>

  <div class="service-grid">
    <div class="tile tile--paint" role="img" aria-label="Foto: Lack vorher und nachher"><span class="tile__label">Lackkorrektur</span></div>
    <div class="tile tile--coat" role="img" aria-label="Foto: glänzende blaue Fahrzeugfront"><span class="tile__label">Lackveredelung</span></div>
    <div class="tile tile--interior" role="img" aria-label="Foto: Mittelkonsole vorher und nachher"><span class="tile__label">Innenraumreinigung</span></div>
    <div class="tile tile--upholstery" role="img" aria-label="Foto: Stoffsitz vorher und nachher"><span class="tile__label">Polsterreinigung</span></div>
    <div class="tile tile--leather" role="img" aria-label="Foto: Ledersitz im Fahrzeug"><span class="tile__label">Lederreinigung</span></div>
    <div class="tile tile--repair" role="img" aria-label="Foto: abgeklebter Ledersitz bei der Reparatur"><span class="tile__label">Lederreparatur</span></div>
  </div>

  <div class="more">
    <p class="more__title">Weitere Leistungen:</p>
    <p class="more__list">Scheibenversiegelung, Bremsenversiegelung, Wachs-Versiegelung,<br>Cabriodachimprägnierung, Scheinwerferaufbereitung, uvm.</p>
  </div>

  <p class="offer">AUSSENAUFBEREITUNG AB</p>
  <p class="price"><span class="price__num">299</span><span class="price__star">*</span><span class="price__cur">€</span></p>
  <p class="footnote">*Alle Preise orientieren sich an<br>einem gepflegten Fahrzeug<br>im Neuwagenzustand.</p>

  <svg class="art" width="515" height="1104" viewBox="0 0 515 1104">
    <defs>
      <linearGradient id="carBack" x1="0" y1="0" x2="1" y2="1">
        <stop offset="0" stop-color="#1b2a55"/>
        <stop offset=".6" stop-color="#0e1630"/>
        <stop offset="1" stop-color="#9a9a98"/>
      </linearGradient>
    </defs>
    <polygon points="0,818 515,1085 515,1104 0,1104" fill="var(--blue)" role="img" aria-label="Foto: Fahrzeugfront, blau eingefärbt"/>
    <polygon points="225,925 300,860 420,840 500,860 515,900 515,1085 300,975" fill="url(#carBack)" role="img" aria-label="Foto: dunkelblauer Kombi auf Pflaster"/>
  </svg>

  <div class="contact">
    <p class="contact__owner">Inh. Kai Vollmer</p>
    <p class="contact__addr">Am Kelterweg 4<br>71384 Weinstadt</p>
    <p class="contact__row">
      <svg viewBox="0 0 24 24"><path d="M6.6 10.8a15.1 15.1 0 0 0 6.6 6.6l2.2-2.2c.3-.3.7-.4 1-.2 1.1.4 2.3.6 3.6.6.6 0 1 .4 1 1V20c0 .6-.4 1-1 1A17 17 0 0 1 3 4c0-.6.4-1 1-1h3.5c.6 0 1 .4 1 1 0 1.3.2 2.5.6 3.6.1.3 0 .7-.2 1z" fill="var(--white)"/></svg>
      +49 170 318 2296
    </p>
    <p class="contact__row">
      <svg viewBox="0 0 24 24"><rect x="2" y="5" width="20" height="14" rx="1" fill="var(--white)"/><polyline points="2,6 12,13 22,6" fill="none" stroke="var(--blue)" stroke-width="2"/></svg>
      info@vkglanzwerk.de
    </p>
  </div>
  <p class="contact__site">www.vkglanzwerk.de</p>
</section>

</body>
</html>
```